Australian Based Booking Platform Needs Playful Home Page & Profile Page To Showcase Our Acti...

COMPANY OVERVIEW:
WANDER-ON TICKETS is an Australian based activity booking platform. Our point of difference is our Kiosk machines that are located in hotels around Australia and allow customers instant access to book activities from the hotel reception.

HOME PAGE:
This page needs to clearly show that we are Australia’s leading booking platform.
Our Competition: https://www.roamplicity.com.au/en
IMPORTANT SECTIONS ON THE HOME PAGE:
- Key Bullet Points (Best Price Guaranteed, Trusted By Thousands, Australian Owned, Unbeatable Support)
- Top Experiences – (Images of selected experiences in a slider format)
- Take Me There – Gold Coast, Carins, Port Duglas, Sunshine Coast, Whitsundays, Brisbane, Sydney, Adelaide, Hobart, Perth
- Top Deals For You – (Images of selected experiences in a slider format)
- Experiences You’ll Love – (Categories of Adventure Tours, Outdoor Activities, Hot Deals, Fun & Games, Zoos & Aquariums, Reef & Island Cruises)
- Testimonials – (some sort of slider format)
- Top New Experience – (Images of selected experiences in a slider format)
- Footer Menu
NOTE: Including some sort of mascot on the page to introduce a personality would be amazing. A Kangaroo or Koala could be a good choice.

REGION PAGE:
This page needs to clearly show what is on offer in the region. The layout of this page will be used for all regions in Australia (eg Gold Coast, Carins, Port Duglas, Sunshine Coast, Whitsundays, Brisbane, Sydney, Adelaide, Hobart, Perth)
IMPORTANT SECTIONS ON THE REGION PAGE:
- Categories: Adventure Tours, Outdoor Activities, Hot Deals, Fun & Games, Zoos & Aquariums, Reef & Island Cruises
o This Categories menu allows you to flick between sliders with activities from the different categories
- Footer Menu

PROFILE PAGE:
The layout of this page is going to be used to clearly show off every activity people can book.
Competitors Example:
https://www.trekvane.com/tours/Sydney/Sydney-Harbour-Northern-beaches-and-National-Park/d482-559213K7
https://www.roamplicity.com.au/en/gold-coast/bellwick-isle-seal-and-corvana-reefs-snorkelling-cruise
IMPORTANT SECTIONS ON THE PROFILE PAGE:
- Tour Title
- Photos / Video
- Booking Calanda (As displayed on the above link)
- Highlights & Inclusions
- Overview
- Location (Map)
- What To Bring
- Additional Information
- Booking Information
- Reviews:
- Terms & Conditions
NOTE: This page is to be displayed on a kiosk with the following dimensions;
- 1209.8mm x 680.4mm
- Aspect Ratio 16:9

I have uploaded some images of Australia, as well as our logo. Please feel free to use or not use these images as you decide.
Updates

Keep up the good work on the designs :)

Target Market(s)

Australian Holiday Makers

Industry/Entity Type

Tourism Booking Platform

Number of Pages Required

3 page

Font styles to use
Sans Serif

Requirements
Must have
• - This booking calendar https://app.clipvault.com/kR7tWmZ2Lpq9
Nice to have
• A mascot or something to add character to the page.

```html
<!DOCTYPE html>
<html lang="en">
<head>
<meta charset="utf-8">
<title>Wander-On Tickets — Home</title>
<link rel="stylesheet" href="https://fonts.googleapis.com/css2?family=Nunito:wght@400;600;700;800;900&display=swap">
<style>
:root{
  --orange:#f7a21b;
  --orange-deep:#ee8d0c;
  --peach:#fde7c2;
  --peach-soft:#fff4e2;
  --ink:#1c1c28;
  --muted:#55575f;
  --line:#e3e3e6;
  --grey-box:#efefef;
  --red:#e0262b;
  --star:#f5a400;
  --white:#ffffff;
  --black:#050505;
}
*{box-sizing:border-box;margin:0;padding:0}
html,body{width:1200px;height:4436px;overflow:hidden}
body{position:relative;background:var(--white);font-family:"Nunito",sans-serif;color:var(--ink)}
.abs{position:absolute}

/* header + hero */
.hero{left:0;top:0;width:1200px;height:540px;background:linear-gradient(160deg,#1f4a4c 0%,#2f6f6a 40%,#4c8c8a 70%,#9fb7b3 100%)}
.hero-shade{left:0;top:0;width:1200px;height:540px;background:linear-gradient(90deg,rgba(0,0,0,.45),rgba(0,0,0,0) 60%)}
.hero-wave{left:0;top:440px;width:1200px;height:110px}
.brand{left:100px;top:24px;color:var(--white);font-weight:900;font-size:30px;letter-spacing:.5px;line-height:1}
.brand small{display:block;font-size:12px;font-weight:900;letter-spacing:3px;margin-top:4px;text-align:center}
.nav{left:415px;top:34px;display:flex;gap:40px;color:var(--white);font-size:15px;font-weight:600}
.nav-icons{left:885px;top:32px;display:flex;gap:24px}
.btn{background:var(--orange);color:var(--ink);font-weight:700;border-radius:6px;display:flex;align-items:center;justify-content:center}
.login{left:995px;top:24px;width:100px;height:40px;font-size:15px}
.hero-kicker{left:40px;top:150px;color:var(--white);font-size:30px;font-weight:700}
.hero-title{left:40px;top:188px;color:var(--white);font-size:46px;font-weight:900}
.hero-text{left:40px;top:258px;width:420px;color:var(--white);font-size:14px;line-height:1.45}
.get-started{left:100px;top:340px;width:140px;height:44px;font-size:16px}
.slide-arrow{width:36px;height:36px;border-radius:50%;background:var(--white);display:flex;align-items:center;justify-content:center}
.mascot{background:linear-gradient(180deg,#d99a3d,#b9722a);border-radius:46% 46% 38% 38%}

/* features */
.feature{top:578px;width:232px;height:120px}
.feature-label{height:52px;background:var(--grey-box);border-radius:6px;display:flex;align-items:center;padding-left:16px;font-weight:700;font-size:17px}
.feature-icon{margin:14px 0 0 16px;width:52px;height:44px;background:var(--orange);border-radius:6px;display:flex;align-items:center;justify-content:center}

/* section titles */
.section-title{font-size:40px;font-weight:900;color:var(--ink)}
.title-rule{height:4px;background:var(--orange);border-radius:2px}
.pager{display:flex;gap:12px}
.pager span{width:40px;height:40px;border-radius:50%;border:2px solid var(--line);display:flex;align-items:center;justify-content:center;background:var(--white)}

/* activity cards */
.card{width:232px}
.card-photo{height:166px;border-radius:10px}
.card-name{margin-top:14px;font-size:15px;font-weight:700;line-height:1.3}
.card-price{margin-top:10px;font-size:14px;color:var(--muted)}
.card-price s{color:var(--red);margin:0 4px}
.card-price b{font-size:24px;color:var(--ink);font-weight:800}
.card-rating{margin-top:8px;color:var(--star);font-size:15px;letter-spacing:1px}
.card-rating em{font-style:normal;color:var(--muted);font-size:13px;margin-left:6px;letter-spacing:0}

/* destinations band */
.dest-band{left:0;top:1220px;width:1200px;height:440px;background:var(--peach-soft)}
.dest-top{left:0;top:1220px;width:1200px;height:110px;background:linear-gradient(180deg,var(--orange),#fbc46c)}
.dest{top:1356px;height:212px;border-radius:8px}
.dest-name{top:1598px;font-size:30px;font-weight:800;text-align:center}

/* categories */
.love-band{left:0;top:2180px;width:1200px;height:800px;background:linear-gradient(180deg,var(--orange) 0%,#fcc978 35%,var(--peach) 60%,var(--white) 100%)}
.cat{width:290px;height:290px;border-radius:50%;display:flex;align-items:center;justify-content:center;text-align:center;color:var(--white);font-size:19px;font-weight:800;padding:0 40px;box-shadow:0 8px 18px rgba(0,0,0,.18)}

/* testimonials */
.quote{top:3140px;width:316px;height:250px;border:2px solid var(--line);border-radius:12px;padding:22px 24px;background:var(--white)}
.quote-mark{color:var(--orange);font-size:44px;font-weight:900;line-height:.6}
.quote-text{margin-top:12px;font-size:14px;line-height:1.45;color:var(--muted)}
.quote-stars{margin-top:10px;color:var(--star);font-size:18px;letter-spacing:2px}
.avatar{right:22px;bottom:18px;width:58px;height:58px;border-radius:50%;background:linear-gradient(180deg,#a7a7a7,#6f6f6f)}

.new-band{left:0;top:3790px;width:1200px;height:210px;background:linear-gradient(180deg,var(--white),var(--peach) 60%,#fbc978)}

/* footer */
.footer{left:0;top:4000px;width:1200px;height:436px;background:var(--black);color:var(--white)}
.contact{top:4064px;display:flex;align-items:center;gap:14px}
.contact-icon{width:44px;height:44px;border-radius:50%;background:#1e1e1e;display:flex;align-items:center;justify-content:center}
.contact-label{font-size:11px;color:var(--orange);letter-spacing:1px;font-weight:700}
.contact-value{font-size:15px;margin-top:2px}
.foot-brand{left:0;top:4172px;width:1200px;text-align:center;font-weight:900;font-size:58px;color:var(--white);line-height:1}
.foot-brand small{display:block;font-size:18px;letter-spacing:6px;margin-top:6px}
.foot-rule{left:100px;top:4340px;width:1000px;height:1px;background:#333}
.copyright{left:0;top:4376px;width:1200px;text-align:center;font-size:15px;color:#ddd}
</style>
</head>
<body>

<!-- Header & hero -->
<div class="abs hero" role="img" aria-label="Jet boat carving a white spray across turquoise water beside green hills"></div>
<div class="abs hero-shade"></div>
<svg class="abs hero-wave" viewBox="0 0 1200 110" preserveAspectRatio="none"><path d="M0 60 C300 120 700 0 1200 50 L1200 110 L0 110 Z" fill="#ffffff"/></svg>
<div class="abs mascot" style="left:905px;top:150px;width:230px;height:340px" role="img" aria-label="Kangaroo mascot in a flag-print shirt waving"></div>

<div class="abs brand">WANDER-ON<small>TICKETS</small></div>
<nav class="abs nav"><span>Destinations</span><span>Experiences</span><span>Hot Deals</span><span>Gifts</span></nav>
<div class="abs nav-icons">
  <svg width="22" height="22" viewBox="0 0 24 24" fill="none" stroke="#fff" stroke-width="2.4"><circle cx="10" cy="10" r="7"/><path d="M15 15l6 6"/></svg>
  <svg width="22" height="22" viewBox="0 0 24 24" fill="#fff"><path d="M2 3h3l3 12h11l3-9H7" stroke="#fff" stroke-width="2" fill="none"/><circle cx="9" cy="20" r="2"/><circle cx="18" cy="20" r="2"/></svg>
</div>
<div class="abs btn login">Login</div>

<div class="abs hero-kicker">Welcome to</div>
<h1 class="abs hero-title">Wander-On Tickets</h1>
<p class="abs hero-text">Lorem ipsum dolor sit amet, consectetur adipiscing elit, sed do eiusmod tempor incididunt ut labore et dolore magna aliqua.</p>
<div class="abs btn get-started">Get Started</div>
<div class="abs slide-arrow" style="left:22px;top:262px"><svg width="14" height="14" viewBox="0 0 14 14"><path d="M9 2L4 7l5 5" stroke="#1c1c28" stroke-width="2.4" fill="none"/></svg></div>
<div class="abs slide-arrow" style="left:1142px;top:262px"><svg width="14" height="14" viewBox="0 0 14 14"><path d="M5 2l5 5-5 5" stroke="#1c1c28" stroke-width="2.4" fill="none"/></svg></div>

<!-- Key points -->
<div class="abs feature" style="left:100px"><div class="feature-label">Best Price Guaranteed</div><div class="feature-icon"><svg width="24" height="24" viewBox="0 0 24 24" fill="none" stroke="#1c1c28" stroke-width="2"><path d="M3 12l9-9h8v8l-9 9z"/><circle cx="16" cy="8" r="1.6"/></svg></div></div>
<div class="abs feature" style="left:356px"><div class="feature-label">Trusted By Thousands</div><div class="feature-icon"><svg width="24" height="24" viewBox="0 0 24 24" fill="none" stroke="#1c1c28" stroke-width="2"><path d="M12 3l7 3v6c0 4-3 7-7 9-4-2-7-5-7-9V6z"/><path d="M8.5 12l2.5 2.5 4.5-5"/></svg></div></div>
<div class="abs feature" style="left:612px"><div class="feature-label">Australian Owned</div><div class="feature-icon"><svg width="24" height="24" viewBox="0 0 24 24" fill="none" stroke="#1c1c28" stroke-width="2"><path d="M4 21V4M4 4h13l-3 4 3 4H4"/></svg></div></div>
<div class="abs feature" style="left:868px"><div class="feature-label">Unbeatable Support</div><div class="feature-icon"><svg width="24" height="24" viewBox="0 0 24 24" fill="none" stroke="#1c1c28" stroke-width="2"><path d="M4 14v-2a8 8 0 0116 0v2"/><rect x="3" y="13" width="4" height="6" rx="1"/><rect x="17" y="13" width="4" height="6" rx="1"/></svg></div></div>

<!-- Top Experiences -->
<h2 class="abs section-title" style="left:100px;top:766px">Top Experiences</h2>
<div class="abs title-rule" style="left:100px;top:826px;width:1000px;height:1px;background:var(--line)"></div>
<div class="abs title-rule" style="left:100px;top:824px;width:90px"></div>
<div class="abs pager" style="left:1008px;top:774px"><span><svg width="12" height="12" viewBox="0 0 12 12"><path d="M8 1L3 6l5 5" stroke="#1c1c28" stroke-width="2" fill="none"/></svg></span><span><svg width="12" height="12" viewBox="0 0 12 12"><path d="M4 1l5 5-5 5" stroke="#1c1c28" stroke-width="2" fill="none"/></svg></span></div>

<div class="abs card" style="left:100px;top:866px"><div class="card-photo" role="img" aria-label="Kayaking on a calm green river" style="background:linear-gradient(160deg,#3f6b55,#8aa57a)"></div><p class="card-name">Nemo enim ipsam voluptatem quia voluptas</p><p class="card-price">from<s>$169.00</s><b>$141.55</b></p><p class="card-rating">★★★★★<em>4.0</em></p></div>
<div class="abs card" style="left:356px;top:866px"><div class="card-photo" role="img" aria-label="Travellers reading a map outdoors" style="background:linear-gradient(160deg,#c9b79a,#7d8f7a)"></div><p class="card-name">Nemo enim ipsam voluptatem quia voluptas</p><p class="card-price">from<s>$169.00</s><b>$141.55</b></p><p class="card-rating">★★★★★<em>4.0</em></p></div>
<div class="abs card" style="left:612px;top:866px"><div class="card-photo" role="img" aria-label="Couple taking a holiday selfie in the sun" style="background:linear-gradient(160deg,#e6d2b3,#b99070)"></div><p class="card-name">Nemo enim ipsam voluptatem quia voluptas</p><p class="card-price">from<s>$169.00</s><b>$141.55</b></p><p class="card-rating">★★★★★<em>4.0</em></p></div>
<div class="abs card" style="left:868px;top:866px"><div class="card-photo" role="img" aria-label="Turquoise bay with limestone islands" style="background:linear-gradient(160deg,#6fbfd0,#2c7f78)"></div><p class="card-name">Nemo enim ipsam voluptatem quia voluptas</p><p class="card-price">from<s>$169.00</s><b>$141.55</b></p><p class="card-rating">★★★★★<em>4.0</em></p></div>

<!-- Take Me There -->
<div class="abs dest-band"></div>
<div class="abs dest-top"></div>
<div class="abs mascot" style="left:0;top:1140px;width:160px;height:380px" role="img" aria-label="Kangaroo mascot peeking in from the left"></div>
<h2 class="abs section-title" style="left:0;top:1260px;width:1200px;text-align:center">Take Me There</h2>
<div class="abs slide-arrow" style="left:108px;top:1474px;border:2px solid var(--line)"><svg width="12" height="12" viewBox="0 0 12 12"><path d="M8 1L3 6l5 5" stroke="#1c1c28" stroke-width="2" fill="none"/></svg></div>
<div class="abs dest" style="left:168px;width:324px;background:linear-gradient(160deg,#8fb3c7,#5a7a4b)" role="img" aria-label="Theme park roller coaster loops under blue sky"></div>
<div class="abs dest" style="left:512px;width:324px;background:linear-gradient(160deg,#cfd89a,#3c5a2e)" role="img" aria-label="Sunlit rainforest path in the tropics"></div>
<div class="abs dest" style="left:856px;width:344px;background:linear-gradient(160deg,#9cc6e0,#4d7d8f)" role="img" aria-label="Coastal town overlooking a blue bay"></div>
<div class="abs dest-name" style="left:168px;width:324px">Gold Coast</div>
<div class="abs dest-name" style="left:512px;width:324px">Carins</div>
<div class="abs dest-name" style="left:856px;width:344px">Port Douglas</div>

<!-- Top Deals -->
<h2 class="abs section-title" style="left:100px;top:1702px">Top Deals For You</h2>
<div class="abs title-rule" style="left:100px;top:1762px;width:1000px;height:1px;background:var(--line)"></div>
<div class="abs title-rule" style="left:100px;top:1760px;width:90px"></div>
<div class="abs pager" style="left:1008px;top:1710px"><span><svg width="12" height="12" viewBox="0 0 12 12"><path d="M8 1L3 6l5 5" stroke="#1c1c28" stroke-width="2" fill="none"/></svg></span><span><svg width="12" height="12" viewBox="0 0 12 12"><path d="M4 1l5 5-5 5" stroke="#1c1c28" stroke-width="2" fill="none"/></svg></span></div>

<div class="abs card" style="left:100px;top:1792px"><div class="card-photo" role="img" aria-label="Resort lounge with ocean view" style="background:linear-gradient(160deg,#d7c6a8,#8a7056)"></div><p class="card-name">Nemo enim ipsam voluptatem quia voluptas</p><p class="card-price">from<s>$169.00</s><b>$141.55</b></p><p class="card-rating">★★★★★<em>4.0</em></p></div>
<div class="abs card" style="left:356px;top:1792px"><div class="card-photo" role="img" aria-label="Hotel terrace lit at dusk" style="background:linear-gradient(160deg,#4b3d35,#c08a4c)"></div><p class="card-name">Nemo enim ipsam voluptatem quia voluptas</p><p class="card-price">from<s>$169.00</s><b>$141.55</b></p><p class="card-rating">★★★★★<em>4.0</em></p></div>
<div class="abs card" style="left:612px;top:1792px"><div class="card-photo" role="img" aria-label="Traveller checking in at a hotel reception" style="background:linear-gradient(160deg,#e5e1dc,#9a8f86)"></div><p class="card-name">Nemo enim ipsam voluptatem quia voluptas</p><p class="card-price">from<s>$169.00</s><b>$141.55</b></p><p class="card-rating">★★★★★<em>4.0</em></p></div>
<div class="abs card" style="left:868px;top:1792px"><div class="card-photo" role="img" aria-label="Hotel room with a city window" style="background:linear-gradient(160deg,#b9a48d,#5f4a3b)"></div><p class="card-name">Nemo enim ipsam voluptatem quia voluptas</p><p class="card-price">from<s>$169.00</s><b>$141.55</b></p><p class="card-rating">★★★★★<em>4.0</em></p></div>

<!-- Experiences You'll Love -->
<div class="abs love-band"></div>
<h2 class="abs section-title" style="left:100px;top:2236px">Experiences You’ll Love</h2>
<div class="abs title-rule" style="left:100px;top:2296px;width:1000px;height:1px;background:rgba(28,28,40,.2)"></div>
<div class="abs title-rule" style="left:100px;top:2294px;width:90px;background:var(--ink)"></div>

<div class="abs cat" style="left:190px;top:2366px;background:radial-gradient(circle at 50% 35%,#7f8f78,#2f3a30)" role="img" aria-label="Rafting through white water">Categories of Adventure Tours</div>
<div class="abs cat" style="left:455px;top:2366px;background:radial-gradient(circle at 50% 35%,#8c9a6a,#34402a)" role="img" aria-label="Mountain biking on a forest trail">Outdoor Activities</div>
<div class="abs cat" style="left:720px;top:2366px;background:radial-gradient(circle at 50% 35%,#d9b48e,#6b4a34)" role="img" aria-label="Friends laughing together on holiday">Hot Deals, Fun &amp; Games</div>
<div class="abs cat" style="left:300px;top:2660px;background:radial-gradient(circle at 50% 35%,#3f7fa0,#0e2d44)" role="img" aria-label="Shark gliding in an aquarium tank">Zoos &amp; Aquariums</div>
<div class="abs cat" style="left:610px;top:2660px;background:radial-gradient(circle at 50% 35%,#45b3d4,#126080)" role="img" aria-label="Snorkeller underwater over a reef">Reef &amp; Island Cruises</div>
<div class="abs mascot" style="left:1015px;top:2770px;width:170px;height:380px" role="img" aria-label="Kangaroo mascot standing and waving"></div>

<!-- Testimonials -->
<h2 class="abs section-title" style="left:0;top:3046px;width:1200px;text-align:center">Testimonials</h2>
<div class="abs title-rule" style="left:555px;top:3106px;width:90px"></div>
<div class="abs quote" style="left:100px"><div class="quote-mark">“</div><p class="quote-text">Sed ut perspiciatis unde omnis iste natus error sit voluptatem accusantium doloremque laudantium, totam rem aperiam, eaque ipsa quae</p><p class="quote-stars">★★★★★</p><div class="abs avatar" role="img" aria-label="Reviewer portrait"></div></div>
<div class="abs quote" style="left:442px"><div class="quote-mark">“</div><p class="quote-text">Sed ut perspiciatis unde omnis iste natus error sit voluptatem accusantium doloremque laudantium, totam rem aperiam, eaque ipsa quae</p><p class="quote-stars">★★★★★</p><div class="abs avatar" role="img" aria-label="Reviewer portrait"></div></div>
<div class="abs quote" style="left:784px"><div class="quote-mark">“</div><p class="quote-text">“Fantastic alternative to hotel if you plan on being out and about during your stay. Complex is hotel like in its standard, apartment is like a</p><p class="quote-stars">★★★★★</p><div class="abs avatar" role="img" aria-label="Reviewer portrait"></div></div>

<!-- Top New Experience -->
<div class="abs new-band"></div>
<h2 class="abs section-title" style="left:100px;top:3518px">Top New Experience</h2>
<div class="abs title-rule" style="left:100px;top:3578px;width:1000px;height:1px;background:var(--line)"></div>
<div class="abs title-rule" style="left:100px;top:3576px;width:90px"></div>
<div class="abs pager" style="left:1008px;top:3526px"><span><svg width="12" height="12" viewBox="0 0 12 12"><path d="M8 1L3 6l5 5" stroke="#1c1c28" stroke-width="2" fill="none"/></svg></span><span><svg width="12" height="12" viewBox="0 0 12 12"><path d="M4 1l5 5-5 5" stroke="#1c1c28" stroke-width="2" fill="none"/></svg></span></div>

<div class="abs card" style="left:100px;top:3610px"><div class="card-photo" role="img" aria-label="Pool float on bright blue water" style="background:linear-gradient(160deg,#6fd0df,#1d8fb0)"></div><p class="card-name">Nemo enim ipsam voluptatem quia voluptas</p><p class="card-price">from<s>$169.00</s><b>$141.55</b></p><p class="card-rating">★★★★★<em>4.0</em></p></div>
<div class="abs card" style="left:356px;top:3610px"><div class="card-photo" role="img" aria-label="Group of friends enjoying a day out" style="background:linear-gradient(160deg,#e4d6c4,#9c8270)"></div><p class="card-name">Nemo enim ipsam voluptatem quia voluptas</p><p class="card-price">from<s>$169.00</s><b>$141.55</b></p><p class="card-rating">★★★★★<em>4.0</em></p></div>
<div class="abs card" style="left:612px;top:3610px"><div class="card-photo" role="img" aria-label="Excited riders on a theme park ride" style="background:linear-gradient(160deg,#e2a46b,#7a4a2c)"></div><p class="card-name">Nemo enim ipsam voluptatem quia voluptas</p><p class="card-price">from<s>$169.00</s><b>$141.55</b></p><p class="card-rating">★★★★★<em>4.0</em></p></div>
<div class="abs card" style="left:868px;top:3610px"><div class="card-photo" role="img" aria-label="Water slide splash at a waterpark" style="background:linear-gradient(160deg,#9fd7ea,#3b8fb6)"></div><p class="card-name">Nemo enim ipsam voluptatem quia voluptas</p><p class="card-price">from<s>$169.00</s><b>$141.55</b></p><p class="card-rating">★★★★★<em>4.0</em></p></div>

<!-- Footer -->
<footer class="abs footer"></footer>
<div class="abs contact" style="left:170px"><span class="contact-icon"><svg width="20" height="20" viewBox="0 0 24 24" fill="none" stroke="#fff" stroke-width="2"><rect x="3" y="5" width="18" height="14" rx="2"/><path d="M3 7l9 6 9-6"/></svg></span><div><div class="contact-label">EMAIL</div><div class="contact-value">info@wanderontickets.com</div></div></div>
<div class="abs contact" style="left:500px"><span class="contact-icon"><svg width="20" height="20" viewBox="0 0 24 24" fill="none" stroke="#fff" stroke-width="2"><path d="M12 22s7-7 7-12a7 7 0 00-14 0c0 5 7 12 7 12z"/><circle cx="12" cy="10" r="2.5"/></svg></span><div><div class="contact-label">OUR LOCATION</div><div class="contact-value">tempor incididunt ut labore</div></div></div>
<div class="abs contact" style="left:840px"><span class="contact-icon"><svg width="20" height="20" viewBox="0 0 24 24" fill="none" stroke="#fff" stroke-width="2"><path d="M5 3h4l2 5-3 2a11 11 0 006 6l2-3 5 2v4a2 2 0 01-2 2A17 17 0 013 5a2 2 0 012-2z"/></svg></span><div><div class="contact-label">PHONE NUMBER</div><div class="contact-value">+61 400 555 012</div></div></div>
<div class="abs foot-brand">WANDER-ON<small>TICKETS</small></div>
<div class="abs foot-rule"></div>
<p class="abs copyright">© Copyrights 2023 Wander-On Tickets | All Rights Reserved</p>

</body>
</html>
```